National Human Immunology Network Needs a Brochure DesignBrochure Design Project

We need a brochure design for a new Canadian network called VEKO. VEKO stands for "VRSL Cellular Defence Alliance". (VRSL is the Northfield Councils of Medical Inquiry and is the funder of the network).

The VRSL Cellular Defence Alliance (VEKO) is a resource network that facilitates, promotes and enhances research in human immunology and its translation into clinical care and public policy. VEKO is an inclusive National Network with International projections that will act as a coordinating resource for investigators working in different aspects of Human Immunology. As a research network, VEKO will operate as a resource “umbrella” network, facilitating communication between nodes, each with their specialized expertise in human immunology,
collaboration and knowledge exchange.

We have a VEKO logo already designed as well as the text to be used in the brochure. In addition we should include the VRSL logo somewhere on the brochure, but it does need to be front and centre. Thinking that a tri-fold brochure would work best.

Target Market(s)

Researchers, politicians, lay public

Industry/Entity Type

Communication

Requirements
Must have
• Must use logo provided.

```html
<!DOCTYPE html>
<html lang="en">
<head>
<meta charset="utf-8">
<title>VRSL Cellular Defence Alliance – Brochure</title>
<link href="https://fonts.googleapis.com/css2?family=PT+Sans:ital,wght@0,400;0,700;1,400&display=swap" rel="stylesheet">
<style>
  :root {
    --band: #a0ebe6;
    --red: #d5281c;
    --ink: #231f20;
    --mark-grey: #4a4a4a;
    --paper: #ffffff;
    --photo-light: #eef0f2;
    --photo-mid: #c9b8a8;
    --photo-dark: #6c7b8c;
  }
  html, body { margin: 0; padding: 0; overflow: hidden; background: var(--paper); }
  .brochure {
    position: relative;
    width: 1200px; height: 855px;
    overflow: hidden;
    background: var(--paper);
    font-family: "PT Sans", "Myriad Pro", Arial, sans-serif;
    color: var(--ink);
  }
  .band { position: absolute; background: var(--band); }
  .band--top { left: 0; top: 0; width: 1200px; height: 35px; }
  .band--bottom { left: 0; top: 818px; width: 1200px; height: 37px; }
  .band--upper { left: 408px; top: 126px; width: 792px; height: 20px; }
  .band--lower { left: 408px; top: 300px; width: 792px; height: 21px; }

  .story { position: absolute; left: 50px; top: 66px; width: 340px; }
  .story h2 {
    margin: 0 0 6px; color: var(--red);
    font-size: 23px; font-weight: 400; line-height: 1.1;
  }
  .story p { margin: 0 0 12px; font-size: 14.5px; line-height: 1.33; }
  .story .next { margin-top: 4px; }

  .wordmark {
    position: absolute; display: flex; align-items: center; gap: 16px;
    color: var(--mark-grey); font-weight: 700; text-transform: uppercase;
  }
  .wordmark__square { background: var(--red); flex: none; }
  .wordmark--cover { left: 828px; top: 160px; font-size: 27px; line-height: 1.15; }
  .wordmark--cover .wordmark__square { width: 96px; height: 96px; }
  .wordmark--back { left: 496px; top: 716px; font-size: 17px; line-height: 1.15; gap: 12px; }
  .wordmark--back .wordmark__square { width: 62px; height: 62px; }

  .contact { position: absolute; left: 427px; top: 342px; font-size: 14.5px; line-height: 1.35; }
  .contact p { margin: 0 0 14px; }
  .contact b { font-weight: 700; }

  .team-photo {
    position: absolute; left: 803px; top: 336px; width: 397px; height: 482px;
    background: linear-gradient(160deg, var(--photo-light) 0%, var(--photo-mid) 55%, var(--photo-dark) 100%);
  }
</style>
</head>
<body>
<main class="brochure">
  <div class="band band--top"></div>
  <div class="band band--upper"></div>
  <div class="band band--lower"></div>
  <div class="band band--bottom"></div>

  <section class="story">
    <h2>Accomplishments:</h2>
    <p>In its first year of operation, VEKO has made significant strides in the establishment of the network. Accomplishments to date include:</p>
    <p>Establishment and set-up of the administrative coordinating node</p>
    <p>Launch of the VEKO website</p>
    <p>Face-to-face meeting of the node leaders in December 2011, and regular monthly teleconference meetings</p>
    <p>Organization of a satellite symposium on <i>“Immune Regulatory Mechanisms in Health &amp; Disease”</i> at GIMS 2012 in Vancouver in partnership with the Northfield Society for Immune Science</p>
    <p>Formation of an External Advisory Board to provide advice and guidance to the network</p>
    <h2 class="next">Next Steps:</h2>
    <p>As VEKO moves forward into the second year of its mandate, plans are in the works for expansion of the network. In addition, presence at international meetings and conferences will be ramped up to increase the profile of the network. VEKO plans on organizing community events across the country to inform the public of current research in human immunology. Finally, a focus on providing resources to trainees and fellows in the form of training seminars will also be examined as a possible resource that can be provided by VEKO.</p>
  </section>

  <div class="wordmark wordmark--cover">
    <span class="wordmark__square"></span>
    <span>VRSL<br>Cellular<br>Defence<br>Alliance</span>
  </div>

  <section class="contact">
    <p><b>Director:</b> Marcus Ellwood<br>Tel: 555-214-0381<br>Email: marcus.ellwood@harrowgate.edu</p>
    <p><b>Manager:</b> Delia Ostrander<br>Tel: 555-708-4416<br>Email: delia.ostrander@med.kestrelvale.edu</p>
    <p><b>Mailing Address:</b><br>Centre for Cellular Defence<br>2250 Larchmont Ave, Suite 310<br>Kestrelvale University<br>Brindlemoor, ON, Canada&nbsp; K4R 7T9</p>
  </section>

  <div class="team-photo" role="img" aria-label="Photo of two smiling researchers in white lab coats"></div>

  <div class="wordmark wordmark--back">
    <span class="wordmark__square"></span>
    <span>VRSL<br>Cellular<br>Defence<br>Alliance</span>
  </div>
</main>
</body>
</html>
```